Animal Eye Clinic needs a Business card

We are a new veterinary ophthalmology practice (Tessaly Animal Eye Care) and we need a business card designed. We only see animal eyes - we are not a regular veterinary clinic. We already have a logo. We are looking for a professional, good looking business card to hand out to our clients. We are looking for something simple but professional and contemporary. Our logo is likely the only picture/graphic that needs to be on the card.
Updates

Contact Information for Business Card

Marisol Dunkley, BSc, DVM, MSc, DipACVO
Veterinary Ophthalmologist

Phone: 250.418.3097
Email: tessalyanimaleyecare@mailbrook.net
Website: tessalyanimaleyecare.net
Address: 1840 Pellworth Rd
Kelowna, BC, V4T 8M3

Colors

Designer to choose colors to be used in the design.

Requirements
Must have
• Our logo (attached)

```html
<!DOCTYPE html>
<html lang="en">
<head>
<meta charset="utf-8">
<title>Tessaly Animal Eye Care — Business Card</title>
<link rel="stylesheet" href="https://fonts.googleapis.com/css2?family=Open+Sans:wght@400;600;700&display=swap">
<style>
  :root {
    --backdrop: #5b5b5b;
    --card: #7a797a;
    --teal: #1b97a6;
    --white: #ffffff;
    --shadow: rgba(0,0,0,0.35);
  }
  * { margin: 0; padding: 0; box-sizing: border-box; }
  html, body {
    width: 1200px; height: 900px; overflow: hidden;
    background: var(--backdrop);
    font-family: "Open Sans", Arial, sans-serif;
  }
  .stage {
    width: 1200px; height: 900px;
    display: flex; flex-direction: column;
    align-items: center; justify-content: center; gap: 34px;
  }
  .card {
    position: relative;
    width: 700px; height: 400px;
    background: var(--card);
    border-radius: 22px;
    box-shadow: 0 14px 30px var(--shadow);
    overflow: hidden;
    color: var(--white);
  }
  /* Back of card: brand name */
  .card--back { display: flex; align-items: center; justify-content: center; }
  .brand { display: flex; align-items: center; gap: 22px; }
  .brand__dot {
    width: 70px; height: 70px; border-radius: 50%;
    background: var(--teal);
  }
  .brand__name {
    font-size: 38px; font-weight: 700; color: var(--teal);
    letter-spacing: 0.5px;
  }
  /* Front of card: contact details */
  .contact {
    position: absolute; left: 48px; top: 42px; width: 380px;
  }
  .contact__name { font-size: 34px; font-weight: 700; color: var(--teal); line-height: 1.1; }
  .contact__creds { font-size: 11px; margin-top: 6px; letter-spacing: 0.3px; }
  .contact__title { font-size: 16px; margin-top: 4px; }
  .contact__company { font-size: 15px; color: var(--teal); margin-top: 26px; }
  .contact__address { font-size: 17px; line-height: 1.35; margin-top: 2px; }
  .contact__lines { list-style: none; margin-top: 18px; font-size: 16px; line-height: 1.55; }
  .contact__lines li { display: flex; align-items: center; gap: 10px; }
  .contact__lines svg { width: 15px; height: 15px; flex: none; }
  .emblem {
    position: absolute; right: -40px; bottom: -40px;
    width: 330px; height: 330px; border-radius: 50%;
    background: var(--white);
    display: flex; align-items: center; justify-content: center;
  }
  .emblem__dot {
    width: 190px; height: 190px; border-radius: 50%;
    background: var(--teal);
    margin: -30px 0 0 -30px;
  }
</style>
</head>
<body>
<main class="stage">
  <section class="card card--back" aria-label="Card back">
    <div class="brand">
      <span class="brand__dot" aria-hidden="true"></span>
      <span class="brand__name">Tessaly Animal Eye Care</span>
    </div>
  </section>

  <section class="card card--front" aria-label="Card front">
    <div class="contact">
      <h1 class="contact__name">Marisol Dunkley</h1>
      <p class="contact__creds">BSc, DVM, MSc, DipACVO</p>
      <p class="contact__title">Veterinary Ophthalmologist</p>
      <p class="contact__company">Tessaly Animal Eye Care</p>
      <p class="contact__address">1840 Pellworth Rd<br>Kelowna, BC, V4T 8M3</p>
      <ul class="contact__lines">
        <li>
          <svg viewBox="0 0 16 16" aria-hidden="true"><path fill="#1b97a6" d="M3.5 1.5l2.5 0 1 3.5-1.6 1.2a8 8 0 0 0 4.4 4.4L11 9l3.5 1v2.5c0 1-1 2-2 2A11 11 0 0 1 1.5 3.5c0-1 1-2 2-2z"/></svg>
          250.418.3097
        </li>
        <li>
          <svg viewBox="0 0 16 16" aria-hidden="true"><rect x="1" y="3" width="14" height="10" rx="1.5" fill="#1b97a6"/><path d="M1.5 4l6.5 5 6.5-5" stroke="#7a797a" stroke-width="1.4" fill="none"/></svg>
          tessalyanimaleyecare@mailbrook.net
        </li>
        <li>
          <svg viewBox="0 0 16 16" aria-hidden="true"><circle cx="8" cy="8" r="6.5" stroke="#1b97a6" stroke-width="1.5" fill="none"/><path d="M1.5 8h13M8 1.5c-3 3.5-3 9.5 0 13M8 1.5c3 3.5 3 9.5 0 13" stroke="#1b97a6" stroke-width="1.2" fill="none"/></svg>
          tessalyanimaleyecare.net
        </li>
      </ul>
    </div>
    <div class="emblem" aria-hidden="true"><span class="emblem__dot"></span></div>
  </section>
</main>
</body>
</html>
```